KTRV Promo Flyer for Corporate Events

Need a 8 page company overview

Target Market(s)

Creditors and Service Providers

Industry/Entity Type

Credit Card

Font styles to use
Serif

Colors
0455a3
fbf289

Requirements
Must have
• Fantastic Material and Creative
Nice to have
• Creative and personal

```html
<!DOCTYPE html>
<html lang="en">
<head>
<meta charset="utf-8">
<title>KTRV Company Overview</title>
<link href="https://fonts.googleapis.com/css2?family=Montserrat:wght@700&family=Poppins:wght@300;400&display=swap" rel="stylesheet">
<style>
  :root {
    --backdrop: #fdf1d3;
    --brand-blue: #0455a3;
    --deep-blue: #0f3b8f;
    --navy: #112d6e;
    --white: #ffffff;
    --ink: #3a3a3a;
    --sky-top: #6fa6d8;
    --sky-mid: #b8cde3;
    --city: #7e8fa6;
    --foliage: #8c8a3c;
    --dusk-top: #141a2c;
    --dusk-mid: #8a4630;
    --dusk-low: #3a2a24;
  }
  * { margin: 0; padding: 0; box-sizing: border-box; }
  html, body { width: 1200px; height: 1200px; overflow: hidden; }
  body {
    background: var(--backdrop);
    font-family: "Poppins", sans-serif;
    position: relative;
  }
  .page { position: absolute; top: 226px; overflow: hidden; }

  /* Cover */
  .cover { left: 38px; width: 549px; height: 776px; background: var(--white); }
  .cover-header { position: absolute; left: 0; top: 0; width: 100%; height: 154px; background: var(--white); }
  .wordmark {
    position: absolute; left: 0; right: 0; top: 72px;
    display: flex; align-items: center; justify-content: center; gap: 12px;
    font-family: "Poppins", sans-serif; font-weight: 300;
    font-size: 30px; letter-spacing: 3px; color: var(--ink);
  }
  .wordmark-square { width: 14px; height: 14px; background: var(--brand-blue); }
  .wordmark-tag {
    position: absolute; left: 105px; right: 80px; top: 112px;
    display: flex; align-items: center; gap: 6px;
    font-size: 11px; font-weight: 300; color: var(--ink); letter-spacing: .5px;
  }
  .wordmark-tag::before, .wordmark-tag::after { content: ""; flex: 1; height: 1px; background: #777; }
  .cover-photo {
    position: absolute; left: 0; top: 154px; width: 100%; height: 426px;
    background: linear-gradient(180deg, var(--sky-top) 0%, var(--sky-mid) 35%, var(--city) 60%, var(--foliage) 100%);
  }
  .cover-band {
    position: absolute; left: 0; top: 580px; width: 100%; height: 196px;
    background: linear-gradient(180deg, var(--deep-blue) 0%, var(--brand-blue) 100%);
  }
  .tile { position: absolute; }
  .tile.white { background: var(--white); }
  .tile.pale { background: rgba(255,255,255,.75); }
  .tile.blue { background: var(--brand-blue); }
  .tile.mid { background: rgba(4,85,163,.75); }
  .tile.shade { background: rgba(10,30,90,.25); }
  .tile.ghost { background: rgba(255,255,255,.18); }
  .rule { position: absolute; width: 3px; background: var(--white); }
  .cover-title {
    position: absolute; left: 110px; top: 556px;
    font-family: "Montserrat", sans-serif; font-weight: 700;
    font-size: 35px; line-height: 43px; color: var(--white); letter-spacing: .5px;
  }
  .cover-sub {
    position: absolute; left: 108px; top: 624px;
    font-size: 15.5px; color: var(--white); letter-spacing: .3px;
  }

  /* Mission page */
  .mission { left: 618px; width: 547px; height: 774px; }
  .mission-photo {
    position: absolute; inset: 0;
    background:
      radial-gradient(ellipse at 80% 18%, rgba(220,110,70,.75) 0%, transparent 55%),
      linear-gradient(180deg, var(--dusk-top) 0%, #3b3244 22%, var(--dusk-mid) 48%, var(--dusk-low) 75%, #1e1a1a 100%);
  }
  .mission-title {
    position: absolute; left: 62px; top: 52px;
    font-family: "Montserrat", sans-serif; font-weight: 700;
    font-size: 37px; line-height: 44px; color: var(--white); letter-spacing: 1px;
  }
  .mission-panel {
    position: absolute; left: 0; top: 163px; width: 426px; height: 199px;
    border-top-right-radius: 22px;
    background: linear-gradient(90deg, rgba(15,59,143,.95), rgba(4,85,163,.92));
  }
  .panel-heading { position: absolute; left: 61px; font-size: 22px; font-weight: 300; color: var(--white); }
  .panel-text { position: absolute; left: 61px; width: 340px; font-size: 10.5px; line-height: 13.4px; color: var(--white); }
  .difference-heading { position: absolute; left: 206px; top: 612px; font-size: 18px; font-weight: 300; color: var(--white); }
  .difference-text { position: absolute; left: 206px; top: 640px; width: 300px; font-size: 10.5px; line-height: 13.4px; color: var(--white); }
</style>
</head>
<body>

<section class="page cover">
  <header class="cover-header">
    <div class="wordmark"><span class="wordmark-square"></span>KTRV</div>
    <div class="wordmark-tag">Accounts Receivable Management</div>
  </header>
  <div class="cover-photo" role="img" aria-label="City skyline with an observation tower, mountain and autumn trees"></div>

  <div class="tile white" style="left:408px;top:154px;width:44px;height:33px"></div>
  <div class="tile blue" style="left:435px;top:173px;width:77px;height:77px"></div>
  <div class="tile pale" style="left:397px;top:212px;width:38px;height:38px"></div>
  <div class="tile white" style="left:313px;top:259px;width:45px;height:45px"></div>
  <div class="tile mid" style="left:385px;top:250px;width:50px;height:50px"></div>
  <div class="tile pale" style="left:435px;top:250px;width:62px;height:62px"></div>
  <div class="tile pale" style="left:358px;top:304px;width:77px;height:77px"></div>
  <div class="tile blue" style="left:435px;top:312px;width:18px;height:18px"></div>
  <div class="tile mid" style="left:307px;top:328px;width:51px;height:51px"></div>
  <div class="tile blue" style="left:358px;top:379px;width:51px;height:51px"></div>
  <div class="tile white" style="left:408px;top:430px;width:44px;height:44px"></div>

  <div class="cover-band"></div>
  <div class="tile shade" style="left:0;top:690px;width:42px;height:42px"></div>
  <div class="tile shade" style="left:42px;top:690px;width:48px;height:48px"></div>
  <div class="tile shade" style="left:120px;top:690px;width:32px;height:32px"></div>
  <div class="tile shade" style="left:152px;top:722px;width:32px;height:32px"></div>

  <div class="rule" style="left:93px;top:546px;height:97px"></div>
  <h1 class="cover-title">KTRV</h1>
  <p class="cover-sub">Accounts Receivable Management</p>
</section>

<section class="page mission">
  <div class="mission-photo" role="img" aria-label="Aerial view of a city riverside highway with light trails at sunset"></div>

  <div class="tile ghost" style="left:399px;top:52px;width:26px;height:26px"></div>
  <div class="tile ghost" style="left:372px;top:93px;width:26px;height:26px"></div>
  <div class="tile ghost" style="left:346px;top:119px;width:26px;height:26px"></div>
  <div class="tile ghost" style="left:406px;top:119px;width:26px;height:26px"></div>

  <div class="rule" style="left:51px;top:51px;height:77px"></div>
  <h2 class="mission-title">MISSION<br>STATEMENT</h2>

  <div class="mission-panel">
    <h3 class="panel-heading" style="top:2px">Our Mission is Simple</h3>
    <p class="panel-text" style="top:42px">We are, in every aspect, a service organization<br>It is always our mission, and our duty, to serve and protect our clients</p>
    <h3 class="panel-heading" style="top:84px;font-size:19px">Our Goal is Clear</h3>
    <p class="panel-text" style="top:120px">Our goal is to deliver on each client’s definition of the ideal agency relationship – every single day KTRV is a service business whose entire focus is on long-term relationship building, by exceeding goals and expectations of our clients every single day.</p>
  </div>
  <div class="tile mid" style="left:340px;top:163px;width:30px;height:30px"></div>
  <div class="tile mid" style="left:400px;top:223px;width:26px;height:26px"></div>

  <div class="tile ghost" style="left:52px;top:486px;width:48px;height:48px"></div>
  <div class="tile ghost" style="left:100px;top:534px;width:52px;height:52px"></div>
  <div class="tile ghost" style="left:52px;top:586px;width:48px;height:48px"></div>
  <div class="tile ghost" style="left:100px;top:634px;width:52px;height:52px"></div>
  <div class="tile ghost" style="left:152px;top:666px;width:48px;height:48px"></div>

  <h3 class="difference-heading">The KTRV Difference</h3>
  <p class="difference-text">An Empathy-Based and Consultive Approach. Our success in the recovery of debt stems from our strong dedication to honest and ethical collections. We treat everybody and all associates with dignity and respect. Embracing an empathy pace. Cooperative approach to resolving outstanding overdue balances.</p>
</section>

</body>
</html>
```